Italian restaurant needs new site

Need to make our website better.

Must have reservation module

Must be able to sell wine tasting tours and wine pairing tours and intégrate with lumo desk

Blog

Social media

Wandermeter ranking and last review.

Number of Pages Required

1 page

Font styles to use
Serif

Requirements
Must have
• Reservation module
• Marketplace to buy wine pairings and gift certificates
• Wandermeter review
• Chatterbay posts
• All info from old site

```html
<!DOCTYPE html>
<html lang="en">
<head>
<meta charset="utf-8">
<title>Serenza Bistro – Italian Cuisine &amp; Wine Bar</title>
<link rel="stylesheet" href="https://fonts.googleapis.com/css2?family=Cinzel:wght@400;600&family=Open+Sans:wght@400;600;700&family=Oswald:wght@500;600&family=Amatic+SC:wght@700&family=Playfair+Display:ital,wght@0,400;0,700;1,400&display=swap">
<style>
:root{
  --ink:#222;
  --muted:#777;
  --line:#e6e6e6;
  --orange:#f2a23a;
  --red:#c0262c;
  --dark:#2b2b2b;
  --white:#fff;
  --chalk-text:#d8d8d8;
}
*{box-sizing:border-box;margin:0;padding:0}
html,body{width:1200px;height:4580px;overflow:hidden}
body{position:relative;background:var(--white);color:var(--ink);font-family:"Open Sans",Arial,sans-serif;font-size:13px}
.abs{position:absolute}
.ph{position:absolute}

/* hero */
.hero{position:absolute;left:0;top:0;width:1200px;height:672px;background:radial-gradient(ellipse at 60% 30%,#6a4a35 0%,#3a2418 45%,#1b120d 100%)}
.hero .photo{left:0;top:0;width:1200px;height:672px;background:radial-gradient(ellipse at 50% 85%,#c98a4a 0%,rgba(160,90,40,.55) 30%,rgba(0,0,0,0) 60%)}
.nav-logo{left:28px;top:18px;color:var(--white);font-family:"Cinzel",serif;font-size:22px;letter-spacing:1px}
.nav-logo small{display:block;font-size:8px;letter-spacing:2px;margin-top:2px}
.nav{left:470px;top:22px;display:flex;gap:30px;list-style:none}
.nav li{color:var(--white);font-size:11px;letter-spacing:1.5px;font-weight:600;text-transform:uppercase}
.nav li.active{border-bottom:1px solid var(--white);padding-bottom:4px}
.brand{left:0;width:1200px;top:290px;text-align:center;color:var(--white)}
.brand .name{font-family:"Cinzel",serif;font-size:78px;letter-spacing:10px;line-height:1}
.brand .sub{font-family:"Playfair Display",serif;font-style:italic;font-size:30px;margin:4px 0 0 160px}
.brand .tag{display:inline-block;margin-top:8px;padding:4px 14px;border-top:1px solid var(--white);border-bottom:1px solid var(--white);font-size:14px;letter-spacing:3px}
.notch{left:540px;top:632px}

/* reservation */
.reserve{left:0;top:690px;width:1200px;text-align:center}
.reserve h2{font-size:12px;letter-spacing:3px;color:#555;font-weight:400;margin-top:48px}
.reserve .power{font-size:9px;letter-spacing:2px;color:#999;margin-top:14px;text-transform:uppercase}
.fields{left:265px;top:148px;display:flex;gap:68px}
.field{display:flex;align-items:center;gap:18px}
.field .box{width:170px;height:36px;border:1px solid #ccc;border-radius:3px;display:flex;align-items:center;justify-content:space-between;padding:0 10px;font-size:14px}
.find{left:518px;top:222px;width:164px;height:34px;background:var(--dark);color:var(--white);font-size:11px;letter-spacing:1.5px;font-weight:700;display:flex;align-items:center;justify-content:center}
.rule{left:140px;top:994px;width:920px;height:1px;background:var(--line)}
.note{left:135px;top:1028px;width:930px;text-align:center;font-size:14px;line-height:24px;color:#444}

/* shop */
.products-head{left:0;top:1160px;width:1200px;text-align:center}
.products-head .kicker{font-family:"Playfair Display",serif;font-style:italic;color:var(--orange);font-size:13px;margin-top:32px}
.products-head h2{font-family:"Oswald",sans-serif;font-size:22px;letter-spacing:1px;font-weight:600;margin-top:2px}
.tabs{display:flex;justify-content:center;gap:30px;list-style:none;margin-top:20px}
.tabs li{font-size:9px;letter-spacing:1px;color:#555;font-weight:600}
.tabs li.active{color:var(--orange)}
.card{position:absolute;width:280px;height:384px;border:1px solid #f0f0f0;background:var(--white);text-align:center}
.card .img{position:absolute;left:30px;top:60px;width:220px;height:170px;border-radius:6px}
.card .stars{position:absolute;top:280px;width:100%;color:var(--orange);font-size:11px;letter-spacing:2px}
.card .pname{position:absolute;top:326px;width:100%;font-size:11px;font-weight:700;letter-spacing:.5px}
.card .price{position:absolute;top:345px;width:100%;font-size:11px;color:var(--orange)}
.card.hover{box-shadow:0 4px 16px rgba(0,0,0,.15);border-color:#ddd}
.card .actions{position:absolute;left:0;bottom:0;width:100%;height:76px;display:flex}
.card .actions span{flex:1;background:var(--orange);display:flex;align-items:center;justify-content:center;border-right:1px solid rgba(255,255,255,.35)}
.card .actions span.cart{flex:1.3;background:var(--dark);color:var(--white);font-size:8px;font-weight:700;letter-spacing:1px}
.corner{position:absolute;left:0;top:0}

/* specialities */
.special{left:0;top:2183px;width:1200px;height:421px;background:linear-gradient(90deg,#3b2a20 0%,#6a4030 40%,#5a2e1e 60%,#2a211c 100%)}
.special-title{left:0;top:2370px;width:1200px;text-align:center;color:var(--white);font-family:"Cinzel",serif;font-size:34px;letter-spacing:8px;font-weight:600}

/* menu */
.menu-frame{left:61px;top:2712px;width:1084px;height:1290px;border:2px solid #d6d6d6;border-top:none}
.menu-frame-top{top:2712px;height:2px;background:#d6d6d6}
.menu-title{left:440px;top:2665px;width:330px;text-align:center;font-family:"Amatic SC",cursive;font-weight:700;font-size:64px;letter-spacing:3px;background:var(--white)}
.dish{position:absolute;width:650px}
.dish .row{display:flex;align-items:baseline}
.dish h3{font-family:"Oswald",sans-serif;font-weight:600;font-size:27px;color:var(--red);letter-spacing:.5px;white-space:nowrap;line-height:1.2}
.dish .dots{flex:1;border-bottom:4px dotted var(--red);margin:0 8px;transform:translateY(-6px)}
.dish .price{font-family:"Amatic SC",cursive;font-weight:700;font-size:42px;color:var(--orange);line-height:1}
.dish p{font-size:12px;line-height:17px;color:#333;width:470px;margin-top:0}

/* blog, reviews, social strip */
.tile{position:absolute;top:4067px;height:207px;overflow:hidden}
.chalk{background:linear-gradient(160deg,#3a3a3c,#232325)}
.chalk .t{position:absolute;left:0;top:20px;width:100%;text-align:center;color:var(--white);font-family:"Playfair Display",serif;font-style:italic;font-size:22px}
.chalk .body{position:absolute;left:34px;top:62px;width:232px;color:var(--chalk-text);font-size:10px;line-height:15px;text-align:center}
.chalk .body strong{display:block;color:var(--orange);font-size:11px;letter-spacing:1px;margin-bottom:6px}
.chalk .body em{display:block;margin-top:8px;color:#9a9a9a;font-style:normal;font-size:9px}
.tile-cap{position:absolute;font-family:"Oswald",sans-serif;font-weight:600}
.tile-kick{position:absolute;font-family:"Playfair Display",serif;font-style:italic;font-size:9px;color:#666}

/* footer */
.footer{left:0;top:4274px;width:1200px;height:306px;background:var(--dark);color:#bdbdbd}
.fcol{position:absolute;top:56px;font-size:9px;line-height:15px}
.fcol h4{color:var(--white);font-size:11px;letter-spacing:1px;margin-bottom:14px;font-weight:700}
.fcol b{color:var(--white);font-weight:600;display:block;margin-top:6px}
.tags{display:grid;grid-template-columns:repeat(3,auto);gap:6px;width:170px}
.tags span{border:1px solid #555;padding:1px 6px;font-size:8px}
.links{display:grid;grid-template-columns:90px 90px}
.hours div{display:flex;justify-content:space-between;width:200px}
.hours div span:last-child{color:var(--white)}
.happy{margin:18px 0 0 20px;width:160px;border:1px solid #777;text-align:center;padding:8px 0}
.happy strong{display:block;color:var(--white);font-family:"Playfair Display",serif;font-style:italic;font-size:12px}
</style>
</head>
<body>

<header class="hero">
  <div class="ph photo" role="img" aria-label="Photo of a plate of spaghetti on a candle-lit restaurant table with wine glass and warm bokeh lights"></div>
  <div class="abs nav-logo">Serenza<small>BISTRO</small></div>
  <ul class="abs nav">
    <li class="active">Home</li><li>About</li><li>Our Menu</li><li>Gallery</li><li>Reservation</li><li>Shop</li><li>Blog</li><li>Pages</li>
  </ul>
  <div class="abs brand">
    <div class="name">SERENZA</div>
    <div class="sub">Bistro</div>
    <div><span class="tag">ITALIAN CUISINE &amp; WINE BAR</span></div>
  </div>
  <svg class="abs notch" width="120" height="40" viewBox="0 0 120 40"><path d="M0 40 L60 0 L120 40 Z" fill="#fff"/><path d="M52 20 L60 27 L68 20" stroke="#222" stroke-width="2.5" fill="none"/></svg>
</header>

<section class="reserve abs">
  <h2>MAKE A RESERVATION</h2>
  <div class="power">powered by TableNest</div>
  <div class="abs fields">
    <div class="field"><svg width="16" height="16" viewBox="0 0 16 16"><rect x="1" y="3" width="14" height="12" fill="none" stroke="#333" stroke-width="1.5"/><path d="M1 7h14M5 1v4M11 1v4" stroke="#333" stroke-width="1.5"/></svg><div class="box">08/05/2017</div></div>
    <div class="field"><svg width="16" height="16" viewBox="0 0 16 16"><circle cx="8" cy="8" r="7" fill="none" stroke="#333" stroke-width="1.5"/><path d="M8 4v4l3 2" stroke="#333" stroke-width="1.5" fill="none"/></svg><div class="box">7:00 pm <span>▾</span></div></div>
    <div class="field"><svg width="16" height="16" viewBox="0 0 16 16"><circle cx="8" cy="5" r="3.5" fill="#333"/><path d="M1 16c0-5 14-5 14 0z" fill="#333"/></svg><div class="box">2 People <span>▾</span></div></div>
  </div>
  <div class="abs find">FIND A TABLE</div>
</section>
<div class="abs rule"></div>
<p class="abs note">Due to the limited amount of tables in our restaurant, we cannot guarantee a private table. Some reservations will be sat at the bar or communal. If you prefer a table, please call or make a note and we will do our best to accommodate your request.</p>
<svg class="abs" style="left:588px;top:1108px" width="24" height="8" viewBox="0 0 24 8"><path d="M0 4h9M15 4h9" stroke="#999"/><circle cx="12" cy="4" r="2" fill="#999"/></svg>

<section class="abs products-head">
  <svg width="30" height="20" viewBox="0 0 30 20"><path d="M4 16 Q15 -2 26 16 Z" fill="none" stroke="#999" stroke-width="1.5"/><path d="M2 17h26" stroke="#999" stroke-width="1.5"/></svg>
  <div class="kicker">Booked through lumo desk</div>
  <h2>WINE TOURS &amp; GIFTS</h2>
  <ul class="tabs"><li class="active">ALL</li><li>TASTING TOURS</li><li>PAIRING TOURS</li><li>GIFT CERTIFICATES</li><li>WINES</li><li>OTHER</li></ul>
</section>

<article class="card" style="left:15px;top:1328px"><div class="img" role="img" aria-label="Photo for the wine tasting tour, glasses of red and white wine" style="background:linear-gradient(#fff,#e9cfa8 60%,#fff)"></div><div class="stars">★★★★☆</div><div class="pname">WINE TASTING TOUR</div><div class="price">$45.00</div></article>
<article class="card hover" style="left:314px;top:1328px">
  <svg class="corner" width="40" height="40" viewBox="0 0 40 40"><path d="M0 0h40L0 40z" fill="#e0534a"/></svg>
  <div class="img" role="img" aria-label="Photo for the wine pairing tour, pizza slices with a glass of wine" style="background:radial-gradient(circle,#e7953c 0%,#c5642a 45%,#d9b47a 70%,#fff 72%)"></div>
  <div class="stars" style="top:254px">★★★★☆</div>
  <div class="actions">
    <span><svg width="16" height="16" viewBox="0 0 16 16"><circle cx="7" cy="7" r="5" fill="none" stroke="#fff" stroke-width="2"/><path d="M11 11l4 4" stroke="#fff" stroke-width="2"/></svg></span>
    <span class="cart">BOOK THIS TOUR</span>
    <span><svg width="16" height="16" viewBox="0 0 16 16"><path d="M8 14 L2 8 A3.5 3.5 0 0 1 8 3.5 A3.5 3.5 0 0 1 14 8 Z" fill="#fff"/></svg></span>
    <span><svg width="16" height="16" viewBox="0 0 16 16"><path d="M2 14V9M6 14V5M10 14V7M14 14V2" stroke="#fff" stroke-width="2.5"/></svg></span>
  </div>
</article>
<article class="card" style="left:611px;top:1328px"><div class="img" role="img" aria-label="Photo for the gift certificate, caprese board with mozzarella and tomatoes" style="background:linear-gradient(135deg,#6b4a32,#8b6a4a)"></div><div class="stars">★★★★☆</div><div class="pname">GIFT CERTIFICATE</div><div class="price">$50.00</div></article>
<article class="card" style="left:900px;top:1328px"><div class="img" role="img" aria-label="Photo for the cellar tour, rustic bread and cheese" style="background:radial-gradient(circle,#c79a6a,#a8764a 55%,#fff 72%)"></div><div class="stars">★★★★☆</div><div class="pname">CHIANTI CELLAR TOUR</div><div class="price">$55.00</div></article>

<article class="card" style="left:15px;top:1725px"><div class="img" role="img" aria-label="Photo for the pairing dinner, olives and oil on a cutting board" style="background:linear-gradient(#f5e3b8,#d9a24a)"></div><div class="stars">★★★★☆</div><div class="pname">PAIRING DINNER FOR TWO</div><div class="price">$120.00</div></article>
<article class="card" style="left:314px;top:1725px"><div class="img" role="img" aria-label="Photo for the gift certificate, wheat and flour on a table" style="background:radial-gradient(circle,#f0e6d4,#cbb48e 55%,#fff 72%)"></div><div class="stars">★★★★☆</div><div class="pname">GIFT CERTIFICATE</div><div class="price">$100.00</div></article>
<article class="card" style="left:611px;top:1725px"><div class="img" role="img" aria-label="Photo for the Tuscan reds tasting, pizza slices on a wooden board" style="background:radial-gradient(circle,#e7953c 0%,#c5642a 45%,#d9b47a 70%,#fff 72%)"></div><div class="stars">★★★★☆</div><div class="pname">TUSCAN REDS TASTING</div><div class="price">$40.00</div></article>
<article class="card" style="left:900px;top:1725px"><div class="img" role="img" aria-label="Photo for the dessert wine pairing, a dessert with chocolate cookies" style="background:radial-gradient(circle,#8a5a3a,#c9a27a 55%,#fff 72%)"></div><div class="stars">★★★★☆</div><div class="pname">DESSERT WINE PAIRING</div><div class="price">$35.00</div></article>

<section class="ph special" role="img" aria-label="Photo of a bowl of braised meat on a dark dining table with bread and wine"></section>
<h2 class="abs special-title">OUR SPECIALITIES</h2>
<svg class="abs" style="left:589px;top:2518px" width="22" height="32" viewBox="0 0 22 32"><rect x="1" y="1" width="20" height="30" rx="10" fill="none" stroke="#fff" stroke-width="2"/><path d="M11 7v7" stroke="#fff" stroke-width="2"/></svg>

<div class="abs menu-frame"></div>
<div class="abs menu-frame-top" style="left:61px;width:380px"></div>
<div class="abs menu-frame-top" style="left:770px;width:375px"></div>
<h2 class="abs menu-title">OUR MENU</h2>

<div class="ph" role="img" aria-label="Photo of two pepperoni pizzas with basil" style="left:824px;top:2687px;width:351px;height:244px;background:radial-gradient(circle at 40% 55%,#e66a3a 0%,#c9502a 35%,#e8b26a 48%,rgba(255,255,255,0) 50%),radial-gradient(circle at 85% 25%,#e66a3a 0%,#e8b26a 25%,rgba(255,255,255,0) 27%)"></div>
<div class="ph" role="img" aria-label="Photo of a fork lifting a slice of margherita pizza" style="left:0;top:3267px;width:420px;height:320px;background:radial-gradient(circle at 35% 60%,#e9653a 0%,#f0c47a 40%,rgba(255,255,255,0) 52%)"></div>
<div class="ph" role="img" aria-label="Photo of a wine bottle, cheese wedge and tomatoes" style="left:0;top:3725px;width:305px;height:215px;background:radial-gradient(ellipse at 50% 70%,#f3c13a 0%,#7a2a1e 45%,rgba(255,255,255,0) 62%)"></div>
<div class="ph" role="img" aria-label="Photo of fresh pasta nests with basil and tomatoes" style="left:656px;top:3800px;width:544px;height:244px;background:radial-gradient(ellipse at 65% 60%,#f0cf7a 0%,#e3b45a 30%,#4f8a34 46%,rgba(255,255,255,0) 60%)"></div>

<div class="dish" style="left:110px;top:2840px"><div class="row"><h3>LOREM IPSUM</h3><span class="dots"></span><span class="price">$13.99</span></div><p>Lorem ipsum dolor sit amet, consectetur adipiscing elit. Duis molestie euis mod met, nec dapibu Lorem ipsum dolor sit amet, consectetur adipiscing elit.</p></div>
<div class="dish" style="left:110px;top:2930px"><div class="row"><h3>LOREM IPSUM</h3><span class="dots"></span><span class="price">$13.99</span></div><p>Lorem ipsum dolor sit amet, consectetur adipiscing elit. Duis molestie euis mod met, nec dapibu Lorem ipsum dolor sit amet, consectetur adipiscing elit.</p></div>
<div class="dish" style="left:110px;top:3020px"><div class="row"><h3>LOREM IPSUM</h3><span class="dots"></span><span class="price">$13.99</span></div><p>Lorem ipsum dolor sit amet, consectetur adipiscing elit. Duis molestie euis mod met, nec dapibu Lorem ipsum dolor sit amet, consectetur adipiscing elit.</p></div>
<div class="dish" style="left:110px;top:3110px"><div class="row"><h3>LOREM IPSUM</h3><span class="dots"></span><span class="price">$13.99</span></div><p>Lorem ipsum dolor sit amet, consectetur adipiscing elit. Duis molestie euis mod met, nec dapibu Lorem ipsum dolor sit amet, consectetur adipiscing elit.</p></div>
<div class="dish" style="left:110px;top:3200px"><div class="row"><h3>LOREM IPSUM</h3><span class="dots"></span><span class="price">$13.99</span></div><p>Lorem ipsum dolor sit amet, consectetur adipiscing elit. Duis molestie euis mod met, nec dapibu Lorem ipsum dolor sit amet, consectetur adipiscing elit.</p></div>

<div class="dish" style="left:465px;top:3375px"><div class="row"><h3>LOREM IPSUM</h3><span class="dots"></span><span class="price">$13.99</span></div><p>Lorem ipsum dolor sit amet, consectetur adipiscing elit. Duis molestie euis mod met, nec dapibu Lorem ipsum dolor sit amet, consectetur adipiscing elit.</p></div>
<div class="dish" style="left:465px;top:3465px"><div class="row"><h3>LOREM IPSUM</h3><span class="dots"></span><span class="price">$13.99</span></div><p>Lorem ipsum dolor sit amet, consectetur adipiscing elit. Duis molestie euis mod met, nec dapibu Lorem ipsum dolor sit amet, consectetur adipiscing elit.</p></div>
<div class="dish" style="left:465px;top:3555px"><div class="row"><h3>LOREM IPSUM</h3><span class="dots"></span><span class="price">$13.99</span></div><p>Lorem ipsum dolor sit amet, consectetur adipiscing elit. Duis molestie euis mod met, nec dapibu Lorem ipsum dolor sit amet, consectetur adipiscing elit.</p></div>
<div class="dish" style="left:465px;top:3645px"><div class="row"><h3>LOREM IPSUM</h3><span class="dots"></span><span class="price">$13.99</span></div><p>Lorem ipsum dolor sit amet, consectetur adipiscing elit. Duis molestie euis mod met, nec dapibu Lorem ipsum dolor sit amet, consectetur adipiscing elit.</p></div>
<div class="dish" style="left:465px;top:3735px"><div class="row"><h3>LOREM IPSUM</h3><span class="dots"></span><span class="price">$13.99</span></div><p>Lorem ipsum dolor sit amet, consectetur adipiscing elit. Duis molestie euis mod met, nec dapibu Lorem ipsum dolor sit amet, consectetur adipiscing elit.</p></div>

<article class="tile" style="left:0;width:300px;background:#f4f1ec">
  <div class="ph" role="img" aria-label="Blog photo of a plated steak dish" style="left:120px;top:0;width:180px;height:207px;background:radial-gradient(circle at 60% 45%,#6a3e28,#b8a48a 55%,#f4f1ec 72%)"></div>
  <div class="tile-kick" style="left:18px;top:126px">from our blog</div>
  <div class="tile-cap" style="left:18px;top:140px;font-size:18px;color:var(--orange)">WINTER AUTUMN</div>
</article>
<article class="tile chalk" style="left:300px;width:300px">
  <div class="t">Wandermeter</div>
  <div class="body"><strong>RANKED #3 OF 210 IN MILLBROOK</strong>“The pairing tour was the highlight of our trip. Every wine matched the dish perfectly.”<em>Latest review · Giulia R. · 5 of 5</em></div>
</article>
<article class="tile" style="left:600px;width:300px;background:#fff">
  <div class="tile-kick" style="left:28px;top:80px">the taste of a</div>
  <div class="tile-cap" style="left:28px;top:94px;font-size:20px;color:#222">GOOD LIFE</div>
  <div class="ph" role="img" aria-label="Blog photo of a hand holding a bread roll" style="left:160px;top:20px;width:130px;height:180px;background:radial-gradient(circle at 50% 45%,#6a3a20,#c9b6a0 60%,#fff 75%)"></div>
  <svg class="abs" style="left:228px;top:14px" width="36" height="36"><circle cx="18" cy="18" r="18" fill="var(--orange)"/></svg>
</article>
<article class="tile chalk" style="left:900px;width:300px">
  <div class="t">Chatterbay</div>
  <div class="body"><strong>LATEST POST</strong>New autumn tasting tour this Saturday. Five reds, three courses, one long table. Seats are limited.<em>2 hours ago · 48 likes</em></div>
</article>

<footer class="abs footer">
  <div class="fcol" style="left:232px">
    <h4>CONTACT</h4>
    <b>Serenza Bistro</b>
    <div>78 Orchard St, Millbrook, NA</div>
    <div>(555) 210-4417</div>
    <div>hello@serenza.example</div>
    <b>Wine Bar</b>
    <div>12 Vine Row, Millbrook, NA</div>
    <div>(555) 210-4418</div>
    <div>www.serenza.example</div>
  </div>
  <div class="fcol" style="left:421px">
    <h4>POPULAR TAGS</h4>
    <div class="tags"><span>Wine</span><span>Tasting</span><span>Pairing</span><span>Gift cards</span><span>Tours</span><span>Pasta</span><span>Pizza</span><span>Events</span><span>Cellar</span><span>Reds</span></div>
  </div>
  <div class="fcol" style="left:604px">
    <h4>USEFUL LINK</h4>
    <div class="links"><span>Our services</span><span>Team</span><span>Wine tours</span><span>Contact</span><span>Gift cards</span><span>Return policy</span><span>Events</span><span>FAQ</span><span>Blog</span><span>Private dining</span><span>Reservations</span></div>
  </div>
  <div class="fcol hours" style="left:800px">
    <h4>WORKING TIME</h4>
    <div><span>Monday to Friday</span><span>08:00am - 08:00pm</span></div>
    <div><span>Saturday &amp; Sunday</span><span>10:00am - 10:00pm</span></div>
    <div class="happy"><strong>Happy Hours</strong>Daily, wine by the glass half price<br>04:00 pm - 06:00 pm</div>
  </div>
</footer>

</body>
</html>
```